Award-winning book needs animated banner ad

I need an animated banner ad for my novel Valdorrin (see attached cover). Would like to show girl in grass, with slight waving of grass. To the right these words on dark background: A Midwestern girl adrift in a new town becomes engulfed in the struggles of two migrant brothers separated by an implacable border. Somewhere the title Valdorrin should appear in the font used on the book cover. Will run in Readers Monthly. Specs are: Unit measurement Pixels (WxH): 728x90
Maximum Initial Download Fileweight: 150kb
Recommended Animation Length (seconds): 15
Acceptable file types: jpg, gif, or png

```html
<!DOCTYPE html>
<html lang="en">
<head>
<meta charset="utf-8">
<title>Valdorrin — Banner</title>
<link href="https://fonts.googleapis.com/css2?family=Sacramento&family=Lato:ital,wght@0,400;1,400&display=swap" rel="stylesheet">
<style>
  :root {
    --night-deep: #0f1418;
    --night-mid: #1b2227;
    --night-glow: #3a4045;
    --grass-dark: #1f4a1c;
    --grass-mid: #3f7f2f;
    --grass-light: #5f9a45;
    --figure-hair: #b58a5e;
    --figure-coat: #6b3a3a;
    --title-ink: #ffffff;
    --tagline-ink: #d9dde0;
  }
  * { margin: 0; padding: 0; box-sizing: border-box; }
  html, body {
    width: 1200px;
    height: 148px;
    overflow: hidden;
    background: var(--night-deep);
  }
  .banner {
    position: relative;
    width: 1200px;
    height: 148px;
    overflow: hidden;
    background:
      radial-gradient(ellipse 360px 150px at 820px 120px, var(--night-glow) 0%, rgba(58,64,69,0) 70%),
      linear-gradient(180deg, var(--night-deep) 0%, var(--night-mid) 100%);
  }
  .banner__figure {
    position: absolute;
    left: 124px;
    top: 0;
    width: 84px;
    height: 132px;
    border-radius: 40px 40px 10px 10px;
    background: linear-gradient(180deg, var(--figure-hair) 0%, var(--figure-hair) 60%, var(--figure-coat) 78%, var(--figure-coat) 100%);
  }
  .banner__grass {
    position: absolute;
    left: 0;
    bottom: 0;
    width: 1200px;
    height: 48px;
    background: linear-gradient(180deg, rgba(63,127,47,0) 0%, var(--grass-mid) 30%, var(--grass-light) 60%, var(--grass-dark) 100%);
  }
  .banner__tagline {
    position: absolute;
    left: 262px;
    top: 26px;
    width: 560px;
    font-family: "Lato", sans-serif;
    font-style: italic;
    font-weight: 400;
    font-size: 17px;
    line-height: 1.45;
    color: var(--tagline-ink);
  }
  .banner__title {
    position: absolute;
    right: 44px;
    top: 22px;
    font-family: "Sacramento", cursive;
    font-size: 74px;
    line-height: 1;
    font-weight: 400;
    color: var(--title-ink);
    letter-spacing: 1px;
  }
</style>
</head>
<body>
  <div class="banner">
    <div class="banner__figure" role="img" aria-label="Photo of a girl seen in profile, standing in tall grass"></div>
    <div class="banner__grass" role="img" aria-label="Photo of tall green grass along the bottom edge"></div>
    <p class="banner__tagline">A Midwestern girl adrift in a new town becomes engulfed in the struggles of two migrant brothers separated by an implacable border.</p>
    <h1 class="banner__title">Valdorrin</h1>
  </div>
</body>
</html>
```